I have a basketball training business combined with a strength training business. I train professio

I recently saw the cats that won the contest in the strength coach business card competition. I loved the design. I.want a card with my logo that calls attention to my clients as the card that won did to me. I would like to see if I could get a similar design. My logo is what I like although I must say I like the red and black design of the contest winner. perhaps if the smaller lettered portion of my logo coukd be separated from the larger KRT logo. It almost looks like 3M3. I like.the KRT Training and Development portion of it. I need help.

Training

```html
<!DOCTYPE html>
<html lang="en">
<head>
<meta charset="utf-8">
<title>KRT Training and Development – Business Card</title>
<link rel="stylesheet" href="https://fonts.googleapis.com/css2?family=Exo+2:wght@700&family=Montserrat:wght@400;500;800&display=swap">
<style>
  :root {
    --stage: #2b2b2d;
    --card: #141414;
    --card-edge: #1c1c1c;
    --red: #d71f26;
    --white: #ffffff;
    --soft: #e6e6e6;
    --label: #d8d8d8;
  }
  * { margin: 0; padding: 0; box-sizing: border-box; }
  html, body { width: 1000px; height: 1200px; overflow: hidden; }
  body {
    position: relative;
    background: var(--stage);
    font-family: "Montserrat", sans-serif;
    color: var(--white);
  }
  .set-label, .side-label {
    position: absolute;
    font-size: 19px;
    color: var(--label);
  }
  .set-label { top: 30px; left: 903px; }
  .side-label.front { top: 591px; left: 139px; color: var(--white); }
  .side-label.back { top: 1117px; left: 799px; }

  .card {
    position: absolute;
    width: 722px;
    height: 423px;
    background: var(--card);
    border: 1px solid var(--card-edge);
    box-shadow: 0 10px 24px rgba(0,0,0,.45);
  }
  .card.front { left: 140px; top: 120px; }
  .card.back { left: 125px; top: 638px; }

  .wordmark {
    position: absolute;
    left: 0; right: 0;
    top: 131px;
    text-align: center;
    font-weight: 800;
    font-size: 29px;
    letter-spacing: 1.5px;
    text-transform: uppercase;
    color: var(--white);
  }

  .identity {
    position: absolute;
    right: 376px;
    top: 226px;
    text-align: right;
  }
  .identity .name {
    font-family: "Exo 2", sans-serif;
    font-weight: 700;
    font-size: 31px;
    line-height: 36px;
    color: var(--red);
  }
  .identity .role {
    font-weight: 500;
    font-size: 20px;
    line-height: 30px;
  }
  .identity .address {
    margin-top: 8px;
    font-size: 19px;
    line-height: 28px;
    color: var(--soft);
    font-style: normal;
  }

  .divider {
    position: absolute;
    left: 361px;
    top: 218px;
    width: 1px;
    height: 150px;
    background: var(--soft);
  }

  .contacts {
    position: absolute;
    left: 374px;
    top: 230px;
    list-style: none;
  }
  .contacts li {
    display: flex;
    align-items: center;
    height: 33.5px;
    font-size: 19px;
    color: var(--soft);
  }
  .contacts svg {
    width: 18px; height: 18px;
    margin-right: 11px;
    fill: var(--red);
    flex: none;
  }

  .back-mark {
    position: absolute;
    left: 0; right: 0;
    top: 138px;
    text-align: center;
    font-weight: 800;
    font-size: 136px;
    line-height: 130px;
    letter-spacing: 6px;
    color: var(--white);
  }
  .back-url {
    position: absolute;
    left: 0; right: 0;
    top: 280px;
    text-align: center;
    font-size: 19px;
    letter-spacing: 1.6px;
    color: var(--soft);
  }
</style>
</head>
<body>
  <div class="set-label">Set1</div>

  <section class="card front" aria-label="Card front">
    <div class="wordmark">KRT Training and Development</div>

    <div class="identity">
      <div class="name">Dana Whitfield</div>
      <div class="role">Business Owner</div>
      <address class="address">1207 Larkspur Avenue<br>Alder, TX 75010</address>
    </div>

    <div class="divider"></div>

    <ul class="contacts">
      <li>
        <svg viewBox="0 0 24 24" aria-hidden="true"><path d="M6.6 10.8a15.1 15.1 0 0 0 6.6 6.6l2.2-2.2a1 1 0 0 1 1-.25 11.4 11.4 0 0 0 3.6.57 1 1 0 0 1 1 1V20a1 1 0 0 1-1 1A17 17 0 0 1 3 4a1 1 0 0 1 1-1h3.5a1 1 0 0 1 1 1c0 1.25.2 2.45.57 3.57a1 1 0 0 1-.25 1z"/></svg>
        +1-555-014-2290
      </li>
      <li>
        <svg viewBox="0 0 24 24" aria-hidden="true"><path d="M7 2h10a2 2 0 0 1 2 2v16a2 2 0 0 1-2 2H7a2 2 0 0 1-2-2V4a2 2 0 0 1 2-2zm0 3v13h10V5zm5 14.2a1 1 0 1 0 0 .01z"/></svg>
        +1-555-014-2290
      </li>
      <li>
        <svg viewBox="0 0 24 24" aria-hidden="true"><path d="M2 5h20v14H2zm2 2v.5l8 5.5 8-5.5V7zm0 2.9V17h5.2zm16 0L14.8 17H20zM10.9 16.6l-.6.4H4.5zm2.2 0 .6.4h5.8z"/></svg>
        info@krttraining.com
      </li>
      <li>
        <svg viewBox="0 0 24 24" aria-hidden="true"><path d="M12 2a10 10 0 1 0 0 20 10 10 0 0 0 0-20zm0 2c.9 0 2.2 1.8 2.8 5H9.2C9.8 5.8 11.1 4 12 4zM8.9 11h6.2a18 18 0 0 1 0 2H8.9a18 18 0 0 1 0-2zm-2 0a20 20 0 0 0 0 2H4.1a8 8 0 0 1 0-2zm10.2 0h2.8a8 8 0 0 1 0 2h-2.8a20 20 0 0 0 0-2zM12 20c-.9 0-2.2-1.8-2.8-5h5.6c-.6 3.2-1.9 5-2.8 5z"/></svg>
        www.krttraining.com
      </li>
    </ul>
  </section>

  <div class="side-label front">Front</div>

  <section class="card back" aria-label="Card back">
    <div class="back-mark">KRT</div>
    <div class="back-url">www.krttraining.com</div>
  </section>

  <div class="side-label back">Back</div>
</body>
</html>
```